mortgage company professional business card

We would like to revamp our business card. Logos and current card attached.

Target Market(s)

white collar professionals

Industry/Entity Type

Mortgage Lender

Contact Information for Business Card

Looking for a sharp professional feel with white background for business card. No gloss. Looking for emboss.

Requirements
Must have
• -Professional touch
• -Emboss and raised lettering
• -Social media icons
• name, title, Phone, email, NMLS and web
• Complement logo and web

```html
<!DOCTYPE html>
<html lang="en">
<head>
<meta charset="utf-8">
<title>Keystone Lending – Business Card</title>
<link rel="stylesheet" href="https://fonts.googleapis.com/css2?family=Roboto:wght@400;500&family=Roboto+Slab:wght@400;500&display=swap">
<style>
  :root {
    --backdrop: #2a2a2a;
    --card: #ececec;
    --navy: #1d1b57;
    --green: #2ea84a;
    --text: #4a4a4a;
    --rule: #26245e;
  }
  * { margin: 0; padding: 0; box-sizing: border-box; }
  html, body { width: 1200px; height: 960px; overflow: hidden; }
  body { background: var(--backdrop); position: relative; font-family: "Roboto", sans-serif; }

  .card {
    position: absolute;
    width: 600px;
    height: 343px;
    background: var(--card);
    box-shadow: 0 2px 6px rgba(0,0,0,.45);
  }
  .card--front { left: 314px; top: 113px; }
  .card--back { left: 311px; top: 472px; }

  .brand { position: absolute; left: 40px; top: 40px; display: flex; flex-direction: column; gap: 8px; }
  .brand__row { display: flex; align-items: center; gap: 10px; }
  .brand__mark { width: 22px; height: 22px; background: var(--green); }
  .brand__name { font-size: 32px; font-weight: 500; color: var(--navy); letter-spacing: -.5px; }
  .brand__tagline { font-size: 14px; color: #6a6a6a; padding-left: 32px; }

  .person { position: absolute; right: 38px; top: 166px; text-align: right; }
  .person__name { font-family: "Roboto Slab", serif; font-weight: 500; font-size: 26px; color: var(--navy); letter-spacing: 1px; line-height: 1; }
  .person__title { font-family: "Roboto Slab", serif; font-size: 14px; color: var(--green); letter-spacing: .5px; margin-top: 7px; }

  .divider { position: absolute; left: 37px; right: 37px; top: 227px; height: 1px; background: var(--rule); }

  .contacts { position: absolute; left: 38px; top: 242px; list-style: none; }
  .contacts li { display: flex; align-items: center; gap: 8px; font-size: 14.5px; color: var(--text); height: 19px; }
  .contacts svg { width: 14px; height: 14px; fill: var(--navy); flex: none; }

  .license { position: absolute; right: 38px; top: 242px; display: flex; align-items: center; gap: 4px; font-size: 14.5px; color: var(--text); }
  .license svg { width: 17px; height: 15px; fill: var(--navy); }

  .social { position: absolute; right: 38px; top: 288px; display: flex; gap: 2px; list-style: none; }
  .social li { width: 24px; height: 24px; border-radius: 50%; background: var(--navy); }

  .back-brand { position: absolute; left: 0; right: 0; top: 110px; display: flex; justify-content: center; align-items: center; gap: 16px; }
  .back-brand .brand__mark { width: 40px; height: 40px; }
  .back-brand__name { font-size: 48px; font-weight: 500; color: var(--navy); letter-spacing: -.5px; }
  .back-web { position: absolute; left: 0; right: 0; top: 292px; text-align: center; font-size: 14px; letter-spacing: 6px; color: var(--text); }
</style>
</head>
<body>

<section class="card card--front">
  <div class="brand">
    <div class="brand__row">
      <span class="brand__mark"></span>
      <span class="brand__name">Keystone Lending</span>
    </div>
    <span class="brand__tagline">Home loans, clearly.</span>
  </div>

  <div class="person">
    <div class="person__name">DANIEL REYES</div>
    <div class="person__title">CEO/FOUNDER</div>
  </div>

  <div class="divider"></div>

  <ul class="contacts">
    <li><svg viewBox="0 0 24 24"><path d="M6.6 10.8a15.1 15.1 0 0 0 6.6 6.6l2.2-2.2c.3-.3.7-.4 1-.2 1.1.4 2.3.6 3.6.6.6 0 1 .4 1 1V20c0 .6-.4 1-1 1A17 17 0 0 1 3 4c0-.6.4-1 1-1h3.5c.6 0 1 .4 1 1 0 1.3.2 2.5.6 3.6.1.3 0 .7-.2 1z"/></svg>0800 (555) 0142</li>
    <li><svg viewBox="0 0 24 24"><path d="M7 1h10a2 2 0 0 1 2 2v18a2 2 0 0 1-2 2H7a2 2 0 0 1-2-2V3a2 2 0 0 1 2-2zm0 3v14h10V4zm5 15.5a1 1 0 1 0 0 2 1 1 0 0 0 0-2z"/></svg>0800 (555) 0187</li>
    <li><svg viewBox="0 0 24 24"><path d="M2 5h20v14H2zm2 2v.5l8 5 8-5V7l-8 5z"/></svg>daniel@keystonelend.com</li>
    <li><svg viewBox="0 0 24 24"><path d="M12 2a10 10 0 1 0 0 20 10 10 0 0 0 0-20zm-1 17.9A8 8 0 0 1 4.2 10.5L9 15v1a2 2 0 0 0 2 2zm6.9-2.5A2 2 0 0 0 16 16h-1v-3a1 1 0 0 0-1-1H8v-2h2a1 1 0 0 0 1-1V7h2a2 2 0 0 0 2-2v-.4a8 8 0 0 1 2.9 12.8z"/></svg>www.keystonelend.com</li>
  </ul>

  <div class="license">
    <svg viewBox="0 0 24 20"><path d="M12 1 1 11h3v8h6v-6h4v6h6v-8h3z"/></svg>NMLS#0000000
  </div>

  <ul class="social" aria-label="Social media">
    <li></li><li></li><li></li><li></li>
  </ul>
</section>

<section class="card card--back">
  <div class="back-brand">
    <span class="brand__mark"></span>
    <span class="back-brand__name">Keystone Lending</span>
  </div>
  <div class="back-web">www.keystonelend.com</div>
</section>

</body>
</html>
```